Korvel Heating & Air Van Wrap Design

We would like to have your designers have a contest to design our van wrap. We did choose a log from one of your designers and it is amazing! We are doing a 1 on 1 with them but also wanted options from the crowd!
phone for wrap 855 KRV WARM
email korvelair.example

Use the Logo that I have Uploaded

The van to use is a Dalvec Strider Low Roof 130"

Target Market(s)

Air Conditioning and Heating Residential

Industry/Entity Type

Air Conditioning

```html
<!DOCTYPE html>
<html lang="en">
<head>
<meta charset="utf-8">
<title>Korvel Heating &amp; Air – Van Wrap</title>
<link rel="stylesheet" href="https://fonts.googleapis.com/css2?family=Exo+2:ital,wght@0,500;0,800;1,600&display=swap">
<style>
  :root{
    --wrap-blue:#27b4dc;
    --wrap-blue-deep:#1b98bd;
    --wrap-teal:#1f7f96;
    --wrap-white:#f2f2f2;
    --wrap-orange:#e2641c;
    --wrap-brown:#7d3c1a;
    --trim:#2b2b2b;
    --glass:#3c3f44;
    --ink:#1d1d1d;
    --bg:#ffffff;
  }
  html,body{margin:0;padding:0;width:1200px;height:1200px;overflow:hidden;background:var(--bg);}
  .sheet{display:block;width:1200px;height:1200px;}
  .wordmark{font-family:"Exo 2",sans-serif;font-weight:800;fill:var(--ink);}
  .tagline{font-family:"Exo 2",sans-serif;font-weight:500;fill:var(--ink);}
  .phone{font-family:"Exo 2",sans-serif;font-style:italic;font-weight:600;fill:#ffffff;}
  .fill-blue{fill:var(--wrap-blue);}
  .fill-blue-deep{fill:var(--wrap-blue-deep);}
  .fill-white{fill:var(--wrap-white);}
  .fill-orange{fill:var(--wrap-orange);}
  .fill-brown{fill:var(--wrap-brown);}
  .fill-trim{fill:var(--trim);}
  .fill-glass{fill:var(--glass);}
  .stripe-teal{fill:var(--wrap-teal);}
</style>
</head>
<body>
<svg class="sheet" viewBox="0 0 1200 1200" xmlns="http://www.w3.org/2000/svg">
  <defs>
    <clipPath id="side-body">
      <path d="M30,470 L32,400 Q40,345 110,322 L225,195 Q300,108 420,102 L1078,100 Q1104,102 1108,130 L1112,470 Z"/>
    </clipPath>
    <clipPath id="back-body">
      <path d="M100,680 Q102,645 140,642 L490,642 Q526,645 528,680 L530,1020 L98,1020 Z"/>
    </clipPath>
    <linearGradient id="flame-tone" x1="0" y1="0" x2="0" y2="1">
      <stop offset="0.2" stop-color="var(--wrap-orange)"/>
      <stop offset="1" stop-color="var(--wrap-brown)"/>
    </linearGradient>
  </defs>

  <!-- Side elevation -->
  <g class="van-side">
    <g clip-path="url(#side-body)">
      <rect class="fill-white" x="0" y="90" width="1200" height="400"/>
      <polygon class="fill-blue" points="0,90 1200,90 1200,100 1030,100 900,195 80,470 0,470"/>
      <polygon class="fill-blue-deep" points="500,110 880,110 880,180 500,327" opacity="0.35" role="img" aria-label="Scattered snowflake pattern on blue"/>
      <polygon class="stripe-teal" points="275,414 1075,104 1090,104 290,420"/>
      <polygon fill="url(#flame-tone)" points="420,470 1112,205 1112,470" role="img" aria-label="Flame pattern in orange and brown"/>
    </g>
    <path class="fill-glass" d="M250,330 L330,222 Q340,210 360,208 L425,205 Q432,206 432,215 L430,305 L262,345 Z"/>
    <rect class="fill-trim" x="28" y="410" width="1094" height="78" rx="14"/>
    <polygon class="fill-white" points="300,462 420,462 410,484 290,484"/>
    <polygon class="fill-orange" points="410,462 800,462 790,484 400,484"/>
    <polygon class="fill-white" points="460,462 500,462 490,484 450,484"/>
    <polygon class="fill-white" points="520,462 560,462 550,484 510,484"/>
    <circle class="fill-trim" cx="205" cy="490" r="64"/><circle cx="205" cy="490" r="32" fill="#9a9a9a"/>
    <circle class="fill-trim" cx="905" cy="505" r="64"/><circle cx="905" cy="505" r="32" fill="#9a9a9a"/>

    <circle class="fill-orange" cx="815" cy="236" r="66"/>
    <g transform="rotate(-22 605 340)">
      <text class="wordmark" x="605" y="335" font-size="92" text-anchor="middle" letter-spacing="6">KRV</text>
      <text class="tagline" x="605" y="368" font-size="24" text-anchor="middle" letter-spacing="4">HEATING &amp; AIR</text>
    </g>
    <text class="phone" x="1010" y="295" font-size="34" text-anchor="middle" transform="rotate(-18 1010 295)">123-456-789</text>
  </g>

  <!-- Rear elevation -->
  <g class="van-rear">
    <g clip-path="url(#back-body)">
      <rect class="fill-white" x="90" y="640" width="450" height="390"/>
      <polygon class="fill-brown" points="90,780 140,780 180,820 428,820 463,780 540,780 540,1030 90,1030"/>
      <polygon class="fill-orange" points="90,788 136,788 176,830 432,830 467,788 540,788 540,1030 90,1030"/>
      <rect fill="url(#flame-tone)" x="90" y="875" width="450" height="155" role="img" aria-label="Flame pattern in orange and brown"/>
    </g>
    <rect class="fill-trim" x="235" y="632" width="146" height="20" rx="8"/>
    <rect x="88" y="880" width="22" height="140" rx="6" fill="#7a1c22"/>
    <rect x="518" y="880" width="22" height="140" rx="6" fill="#7a1c22"/>
    <rect class="fill-trim" x="80" y="1018" width="468" height="88" rx="10"/>
    <rect class="fill-trim" x="95" y="1100" width="70" height="85" rx="10"/>
    <rect class="fill-trim" x="463" y="1100" width="70" height="85" rx="10"/>
    <circle class="fill-orange" cx="303" cy="718" r="42"/>
    <text class="wordmark" x="303" y="799" font-size="34" text-anchor="middle" letter-spacing="3">KRV</text>
    <text class="tagline" x="303" y="815" font-size="11" text-anchor="middle" letter-spacing="2">HEATING &amp; AIR</text>
    <text class="phone" x="303" y="866" font-size="28" text-anchor="middle">123-456-789</text>
  </g>

  <!-- Front elevation -->
  <g class="van-front">
    <path class="fill-blue" d="M710,660 Q712,638 740,637 L1050,637 Q1078,638 1080,660 L1100,820 Q1140,900 1140,960 L1140,1050 L650,1050 L650,960 Q650,900 690,820 Z"/>
    <path class="fill-glass" d="M705,712 Q708,700 722,700 L1068,700 Q1082,700 1085,712 L1095,835 L695,835 Z"/>
    <rect class="fill-trim" x="610" y="805" width="45" height="85" rx="10"/>
    <rect class="fill-trim" x="1135" y="805" width="45" height="85" rx="10"/>
    <rect class="fill-trim" x="750" y="860" width="105" height="10" rx="4"/>
    <rect class="fill-trim" x="935" y="860" width="105" height="10" rx="4"/>
    <path d="M660,905 Q700,892 740,935 L730,960 Q680,955 662,945 Z" fill="#5a5d62"/>
    <path d="M1130,905 Q1090,892 1050,935 L1060,960 Q1110,955 1128,945 Z" fill="#5a5d62"/>
    <path class="fill-trim" d="M765,920 L1025,920 Q1040,922 1045,940 L1030,1010 Q1025,1022 1010,1022 L780,1022 Q765,1022 760,1010 L745,940 Q750,922 765,920 Z"/>
    <path class="fill-trim" d="M648,1030 L1142,1030 L1142,1140 Q1140,1160 1120,1160 L670,1160 Q650,1160 648,1140 Z"/>
    <rect class="fill-trim" x="650" y="1120" width="70" height="67" rx="10"/>
    <rect class="fill-trim" x="1070" y="1120" width="70" height="67" rx="10"/>
  </g>
</svg>
</body>
</html>
```